Sign Design

We already have a logo, but would like to design 2 x signs.
Sign 1:
Dimensions 1500mm wide x 2500m high.
Information to include on sign: - Clinic name and logo (attached)
- the word "DENTIST "
- Street number (which is 348)
Phone number (which is 6153 4097)

Sign 2:
Dimensions: 800mm wide x 600mm high

```html
<!DOCTYPE html>
<html lang="en">
<head>
<meta charset="utf-8">
<title>Tarrawood Dental Care – Signage</title>
<link rel="stylesheet" href="https://fonts.googleapis.com/css2?family=Montserrat:wght@400;700&display=swap">
<style>
  :root {
    --forest: #146f38;
    --lime: #a2de4a;
    --pale-lime: #dcf4b0;
    --paper: #ffffff;
    --outline: #333333;
  }
  * { margin: 0; padding: 0; box-sizing: border-box; }
  html, body { width: 1200px; height: 1200px; overflow: hidden; background: var(--paper); }
  body { position: relative; font-family: "Montserrat", Arial, sans-serif; }

  .sign-tall {
    position: absolute; left: 72px; top: 116px; width: 573px; height: 956px;
    border: 1px solid var(--lime); background: var(--paper); overflow: hidden;
  }
  .sign-tall__heading {
    position: absolute; top: 58px; left: 0; width: 100%; text-align: center;
    font-weight: 700; font-size: 46px; letter-spacing: 27px; text-indent: 27px;
    color: var(--forest); line-height: 1;
  }
  .sign-tall__number {
    position: absolute; left: 22px; top: 380px;
    font-weight: 700; font-size: 102px; letter-spacing: -3px; color: var(--lime); line-height: 1;
  }
  .sign-tall__name {
    position: absolute; transform-origin: top left; transform: rotate(-90deg);
    color: var(--forest); font-weight: 400; white-space: nowrap; line-height: 1;
  }
  .sign-tall__name--main { left: 246px; top: 567px; font-size: 74px; letter-spacing: -3px; }
  .sign-tall__name--sub { left: 322px; top: 426px; font-size: 40px; letter-spacing: -1px; }
  .sign-tall__mark {
    position: absolute; left: 226px; top: 603px; width: 180px; height: 180px;
    border-radius: 50%; background: var(--pale-lime);
  }
  .sign-tall__stripe { position: absolute; left: 0; bottom: 106px; width: 100%; height: 15px; background: var(--lime); }
  .sign-tall__footer {
    position: absolute; left: 0; bottom: 0; width: 100%; height: 106px; background: var(--forest);
    display: flex; align-items: center; justify-content: center;
    color: var(--lime); font-weight: 700; font-size: 58px; letter-spacing: 3px;
  }

  .sign-small {
    position: absolute; left: 765px; top: 514px; width: 306px; height: 230px;
    border: 1px solid var(--outline); background: var(--paper);
  }
  .sign-small__mark {
    position: absolute; left: 27px; top: 75px; width: 70px; height: 70px;
    border-radius: 50%; background: var(--pale-lime);
  }
  .sign-small__name {
    position: absolute; color: var(--forest); font-weight: 400; white-space: nowrap; line-height: 1;
  }
  .sign-small__name--main { left: 110px; top: 84px; font-size: 33px; letter-spacing: -1.5px; }
  .sign-small__name--sub { left: 168px; top: 117px; font-size: 17px; letter-spacing: -0.5px; }
</style>
</head>
<body>
  <section class="sign-tall" aria-label="Tall street sign">
    <h1 class="sign-tall__heading">DENTIST</h1>
    <div class="sign-tall__number">348</div>
    <div class="sign-tall__name sign-tall__name--main">Tarrawood</div>
    <div class="sign-tall__name sign-tall__name--sub">Dental Care</div>
    <div class="sign-tall__mark" aria-hidden="true"></div>
    <div class="sign-tall__stripe"></div>
    <div class="sign-tall__footer">6153 4097</div>
  </section>

  <section class="sign-small" aria-label="Small door sign">
    <div class="sign-small__mark" aria-hidden="true"></div>
    <div class="sign-small__name sign-small__name--main">Tarrawood</div>
    <div class="sign-small__name sign-small__name--sub">Dental Care</div>
  </section>
</body>
</html>
```